Webdesign für lokalen Pfeilwerk
Zielgruppe
Wir sind ein lokaler Pfeilwerk in Hamburg, welcher in Norddeutschland sehr beliebt ist und bundesweit das Größte Angebot bietet. Durch unseren Online-Shop möchte wir unseren Radius erweitern.
Zielgruppe: Dart Anfänger, Fortgeschrittene sowie Vereine und Unternehmen
Aufgabenstellung
In jedem Fall das Haupt-Element unseres Logo´s, einer Dart-Scheibe.

```html
<!DOCTYPE html>
<html lang="de">
<head>
<meta charset="utf-8">
<title>Pfeilwerk Nord – Start</title>
<link href="https://fonts.googleapis.com/css2?family=Montserrat:wght@400;500;600;700&display=swap" rel="stylesheet">
<style>
:root{
  --red:#e0141b;
  --green:#1e9438;
  --ink:#111;
  --muted:#444;
  --card:#f8f8f8;
  --panel:#f4f4f4;
  --white:#fff;
  --tag:#e6e6e6;
}
*{margin:0;padding:0;box-sizing:border-box}
html,body{width:1200px;height:2596px;overflow:hidden}
body{position:relative;background:var(--white);font-family:'Montserrat',sans-serif;color:var(--ink)}
.abs{position:absolute}
.hero{left:0;top:0;width:1200px;height:675px;background:linear-gradient(120deg,#3a3a3a 0%,#5a5248 40%,#8a7c68 65%,#4a4640 100%)}
.brand{left:28px;top:54px;display:flex;align-items:center;gap:8px;color:var(--white);font-weight:700;font-size:13px}
.brand .dot{width:14px;height:14px;border:2px solid var(--white);border-radius:50%}
.nav{top:26px;left:0;width:1200px;height:16px;color:var(--white);font-size:11.5px}
.nav a{position:absolute;color:inherit;text-decoration:none}
.nav .active{font-weight:700}
.hero-title{left:126px;top:207px;color:var(--white);font-size:33px;font-weight:700;line-height:38px;letter-spacing:-.3px}
.btn{display:flex;align-items:center;justify-content:space-between;width:206px;height:45px;padding:0 18px;font-size:11.5px;font-weight:700;border:2px solid currentColor}
.btn svg{width:8px;height:10px}
.btn-light{color:var(--white)}
.btn-dark{color:var(--ink)}
.news{left:126px;top:538px;width:948px;height:563px;background:var(--card)}
.news-bar{left:126px;top:1094px;width:556px;height:8px;background:var(--red)}
.news h2{position:absolute;left:76px;top:92px;color:var(--red);font-size:15.5px;font-weight:700}
.news .alert{position:absolute;left:76px;top:136px;color:var(--red);font-size:11px;font-weight:500}
.news .body{position:absolute;left:76px;top:178px;width:572px;font-size:8.6px;line-height:11px;color:var(--muted)}
.news .body p{margin-bottom:11.5px}
.tags{position:absolute;left:76px;top:488px;display:flex;gap:8px}
.tags span{background:var(--tag);color:#777;font-size:9px;padding:7px 10px;border-radius:3px}
.about-title{left:126px;top:1249px;font-size:15.5px;font-weight:700}
.about-text{left:308px;top:1205px;width:550px;font-size:11.3px;line-height:13.7px}
.panel{left:167px;top:1428px;width:907px;height:583px;background:var(--panel)}
.photo{top:1355px;height:308px}
.info h3{position:absolute;color:var(--green);font-size:15.5px;font-weight:700}
.label{position:absolute;font-size:9px;color:#333}
.value{position:absolute;font-size:11px;font-weight:600}
.small{position:absolute;font-size:9px;color:#333;line-height:20px}
.promo{left:0;top:2086px;width:1200px;height:409px;background:var(--green)}
.promo h2{position:absolute;left:650px;top:150px;color:var(--white);font-size:22px;font-weight:700;line-height:28px}
.promo-art-faint{left:0;top:110px;width:295px;height:290px;background:rgba(255,255,255,.08)}
.promo-art{left:330px;top:95px;width:182px;height:190px;background:rgba(255,255,255,.22)}
.footer-brand{left:280px;top:2526px;display:flex;align-items:center;gap:8px}
.footer-brand .dot{width:44px;height:44px;border:2px solid var(--ink);border-radius:50%}
.copy{left:358px;top:2524px;font-size:11px;font-weight:500}
.links{left:358px;top:2556px;font-size:9px}
.links a{position:absolute;white-space:nowrap;color:var(--ink);text-decoration:none}
</style>
</head>
<body>

<div class="abs hero" role="img" aria-label="Foto: Dartpfeile stecken in einer Dartscheibe"></div>

<div class="abs brand"><span class="dot"></span>Pfeilwerk Nord</div>

<nav class="abs nav">
  <a class="active" style="left:658px">Start</a>
  <a style="left:730px">Aktuelles</a>
  <a style="left:825px">Über uns</a>
  <a style="left:920px">Kontakt</a>
  <a style="left:1008px">Online-Shop</a>
  <svg class="abs" style="left:1120px;top:0" width="16" height="16" viewBox="0 0 16 16" fill="none" stroke="#fff" stroke-width="1.4"><circle cx="7" cy="7" r="5.5"/><path d="M11 11l4 4"/></svg>
  <svg class="abs" style="left:1160px;top:-1px" width="14" height="16" viewBox="0 0 14 16" fill="none" stroke="#fff" stroke-width="1.4"><circle cx="7" cy="4.5" r="3.5"/><path d="M1 16c0-4 2.5-6.5 6-6.5s6 2.5 6 6.5"/></svg>
</nav>

<h1 class="abs hero-title">Lorem ipsum<br>dolor sit amet.</h1>
<a class="abs btn btn-light" style="left:126px;top:313px">Zum Online-Shop<svg viewBox="0 0 8 10" fill="none" stroke="currentColor" stroke-width="1.4"><path d="M2 1l4 4-4 4"/></svg></a>

<section class="abs news">
  <svg class="abs" style="left:75px;top:48px" width="22" height="22" viewBox="0 0 22 22" fill="none" stroke="#e0141b" stroke-width="1.6"><path d="M11 1.5a9.5 9.5 0 0 1 9.5 9.5v9.5H11A9.5 9.5 0 1 1 11 1.5z"/><path d="M11 9.5v6M11 6v1.4"/></svg>
  <h2>Aktuelles aus unserem Shop</h2>
  <p class="alert">Wichtig! Unser lokaler Shop ist vom 16.12.2020 - 14.02.2021 wegen der Corona-Pandemie leider geschlossen!</p>
  <div class="body">
    <p>Liebe Pfeilwerk Nord Kunden,</p>
    <p>wir dürfen ab dem 20.04.2020 wieder öffnen!<br>Aufgrund der aktuellen Entwicklung des Corona-Virus wird es bis auf weiteres folgenden Ablauf zum Eintritt in unseren Shop geben.</p>
    <p>1. Bitte klopfen, wenn die Tür verschlossen ist.</p>
    <p>2. Zur gleichen Zeit ist der Einlass von nur 4 Personen möglich.</p>
    <p>3. Pro Kunde müssen wir die Einkaufzeit leider auf maximal 15-30 Minuten limitieren, falls andere Kunden vor dem Pfeilwerk warten. Damit die Warteschlange nicht zu groß wird.</p>
    <p>4. Für Euren sicheren Aufenthalt bei uns, halten wir für Euch Einmalhandschuhe sowie Desinfektionsmittel kostenlos bereit!</p>
    <p>5. Bitte haltet wenn möglich im ganzen Shop einen Mindestabstand von 1 - 1,5 Meter ein.</p>
    <p>6. Bitte wenn möglich Bargeldzahlung vermeiden.</p>
    <p>Alle wartenden Kunden können auf unseren Bänken vor dem Pfeilwerk Platz nehmen und bekommen von uns gratis Kaffee oder Soft-Getränke!</p>
    <p>Bitte achtet auch hier auf den Mindestabstand!</p>
    <p>Danke für Euer Verständnis und bleibt gesund.</p>
  </div>
  <div class="tags"><span>#dartswm</span><span>#darts</span></div>
</section>
<div class="abs news-bar"></div>

<svg class="abs" style="left:126px;top:1205px" width="21" height="21" viewBox="0 0 21 21" fill="none" stroke="#111" stroke-width="1.5"><circle cx="10.5" cy="10.5" r="9.5"/><circle cx="10.5" cy="10.5" r="5.5"/><circle cx="10.5" cy="10.5" r="1.8" fill="#111"/></svg>
<h2 class="abs about-title">Das sind wir</h2>
<p class="abs about-text">Lorem ipsum dolor sit amet, consectetur adipiscing elit. Turpis a, non, venenatis urna nunc magna porttitor netus. Morbi tortor sodales sit lectus suspendisse tristique. Tortor sapien, amet, est pellentesque viverra arcu. Fames arcu, sit eget morbi nulla ornare ornare. Egestas integer metus, cursus vestibulum morbi dui amet rutrum. Aenean vel vestibulum venenatis, volutpat adipiscing ac ornare faucibus id. Commodo sodales sed commodo facilisis tincidunt tellus, scelerisque. Gravida semper mattis sed neque sollicitudin lobortis a.</p>

<div class="abs panel"></div>
<div class="abs photo" style="left:126px;width:217px;background:linear-gradient(90deg,#e9e6e0 0%,#8a3b2a 25%,#9b4a36 50%,#d8dde0 80%)" role="img" aria-label="Foto: Ladeneingang mit Backsteinfassade und Schaufenster"></div>
<div class="abs photo" style="left:364px;width:219px;background:linear-gradient(180deg,#2f8a5e 0%,#3c9467 35%,#6b5a48 75%,#4a3a2c 100%)" role="img" aria-label="Foto: Regal mit Dartzubehör vor grüner Wand"></div>
<div class="abs photo" style="left:603px;width:219px;background:linear-gradient(180deg,#eeeeee 0%,#b8b5b0 35%,#5a4c40 75%,#3e3027 100%)" role="img" aria-label="Foto: Verkaufsraum mit Dartscheiben an der Wand"></div>
<div class="abs photo" style="left:843px;width:217px;background:linear-gradient(180deg,#dcdcdc 0%,#9a9692 40%,#4a3c32 80%,#3a2e26 100%)" role="img" aria-label="Foto: Ausstellungsraum mit Dartscheiben und Beleuchtungsringen"></div>

<div class="info">
  <h3 style="left:231px;top:1719px">Öffnungszeiten</h3>
  <span class="label" style="left:231px;top:1762px">Montag bis Samstag</span>
  <span class="value" style="left:231px;top:1780px">12:00 - 18:00 Uhr</span>
  <span class="label" style="left:231px;top:1816px">Sonntag</span>
  <span class="value" style="left:231px;top:1834px">Geschlossen</span>

  <h3 style="left:430px;top:1719px">Kontakt</h3>
  <span class="label" style="left:430px;top:1762px">Tel.</span>
  <span class="value" style="left:430px;top:1780px">040 555 218 40 - 0</span>
  <span class="label" style="left:430px;top:1816px">E-Mail</span>
  <span class="value" style="left:430px;top:1834px">info@pfeilwerk-nord.de</span>
  <span class="label" style="left:626px;top:1762px">Fax</span>
  <span class="value" style="left:626px;top:1780px">040 555 218 40 - 9</span>
  <span class="label" style="left:626px;top:1816px">Internet</span>
  <span class="value" style="left:626px;top:1834px">https://www.pfeilwerk-nord.de</span>

  <h3 style="left:883px;top:1719px">Anfahrt</h3>
  <div class="small" style="left:883px;top:1757px">Pfeilwerk Nord GmbH<br>Beispielweg 12<br>20099 Hamburg</div>
</div>
<a class="abs btn btn-dark" style="left:231px;top:1909px">Kontaktiere uns<svg viewBox="0 0 8 10" fill="none" stroke="currentColor" stroke-width="1.4"><path d="M2 1l4 4-4 4"/></svg></a>

<section class="abs promo">
  <div class="abs promo-art-faint" role="img" aria-label="Illustration: blasser Online-Shop als Hintergrundmotiv"></div>
  <div class="abs promo-art" role="img" aria-label="Illustration: Bildschirm mit Ladenmarkise und Einkaufstasche"></div>
  <h2>Entdecke unseren<br>neuen Online-Shop</h2>
  <a class="abs btn btn-light" style="left:650px;top:227px">Zum Online-Shop<svg viewBox="0 0 8 10" fill="none" stroke="currentColor" stroke-width="1.4"><path d="M2 1l4 4-4 4"/></svg></a>
</section>

<div class="abs footer-brand"><span class="dot"></span></div>
<p class="abs copy">© 2021 — Pfeilwerk Nord GmbH</p>
<nav class="abs links">
  <a style="left:0">Impressum</a>
  <a style="left:81px">Datenschutz</a>
  <a style="left:169px">AGB</a>
  <a style="left:218px">Kontakt</a>
  <a style="left:283px">Versand &amp; Zahlung</a>
  <a style="left:399px">Widerrufsformular</a>
  <a style="left:513px">Callback Service</a>
</nav>

</body>
</html>
```